Business Card Design

Sports massage therapist
Would like to convey a simple message.
graphic of human anatomy/muscular system
colours: orange with white/and or grey
glossey

Industry/Entity Type

Business

Contact Information for Business Card

Rhona Whitlow
Soft Tissue Therapist
Sports and Remedial Massage
07915 468302
whitlow.rhona@mailbrook.co.uk

```html
<!DOCTYPE html>
<html lang="en">
<head>
<meta charset="UTF-8">
<title>Rhona Whitlow – Business Card</title>
<link rel="stylesheet" href="https://fonts.googleapis.com/css2?family=Lato:wght@400;700&display=swap">
<style>
  :root {
    --backdrop: #2b2b2b;
    --card: #f2f2f2;
    --card-edge: #e4e4e4;
    --orange: #e0731a;
    --orange-deep: #c85a0c;
    --grey-text: #8a8a8a;
    --dark-text: #2e2e2e;
    --band-grey: #4a4a4a;
    --muscle-light: #e7c3b4;
    --muscle-mid: #c4644a;
    --muscle-deep: #9a3a26;
  }
  * { margin: 0; padding: 0; box-sizing: border-box; }
  html, body {
    width: 1200px;
    height: 1116px;
    overflow: hidden;
    background: var(--backdrop);
    font-family: "Lato", sans-serif;
  }
  .stage {
    width: 1200px;
    height: 1116px;
    display: flex;
    align-items: center;
    justify-content: center;
  }
  .card {
    position: relative;
    width: 1000px;
    height: 572px;
    background: linear-gradient(160deg, #ffffff 0%, var(--card) 55%, var(--card-edge) 100%);
    overflow: hidden;
  }
  .anatomy-art {
    position: absolute;
    left: 0;
    top: 110px;
    width: 470px;
    height: 436px;
    background: radial-gradient(ellipse at 45% 45%, var(--muscle-mid) 0%, var(--muscle-deep) 35%, var(--muscle-light) 70%, rgba(231,195,180,0) 100%);
  }
  .identity {
    position: absolute;
    right: 60px;
    top: 60px;
    text-align: right;
  }
  .identity .name {
    color: var(--orange);
    font-weight: 700;
    font-size: 40px;
    line-height: 1.2;
  }
  .identity .role {
    color: var(--grey-text);
    font-size: 24px;
    line-height: 1.4;
  }
  .identity .service {
    color: var(--dark-text);
    font-size: 25px;
    line-height: 1.3;
  }
  .contact {
    position: absolute;
    right: 150px;
    top: 300px;
    text-align: right;
    color: var(--dark-text);
    font-size: 30px;
    line-height: 1.9;
  }
  .contact-tab {
    position: absolute;
    right: 0;
    top: 262px;
    width: 96px;
    height: 140px;
    background: var(--orange-deep);
    border-radius: 14px 0 0 14px;
    display: flex;
    flex-direction: column;
    align-items: center;
    justify-content: space-evenly;
  }
  .contact-tab svg { width: 40px; height: 40px; }
  .band-grey {
    position: absolute;
    left: 0;
    bottom: 0;
    width: 600px;
    height: 26px;
    background: var(--band-grey);
  }
  .band-orange {
    position: absolute;
    right: 0;
    bottom: 0;
    width: 470px;
    height: 46px;
    background: var(--orange-deep);
    border-top-left-radius: 40px;
  }
</style>
</head>
<body>
<main class="stage">
  <section class="card">
    <div class="anatomy-art" role="img" aria-label="Illustration of a running human figure showing the muscular and skeletal system"></div>

    <header class="identity">
      <p class="name">Rhona Whitlow</p>
      <p class="role">Soft Tissue Therapist</p>
      <p class="service">Sports and Remedial Massage</p>
    </header>

    <div class="contact">
      <p class="phone">07915 468302</p>
      <p class="email">whitlow.rhona@mailbrook.co.uk</p>
    </div>

    <div class="contact-tab">
      <svg viewBox="0 0 40 40" aria-hidden="true">
        <path d="M6 14c0-4 6-7 14-7s14 3 14 7v3h-8v-4c-2-1-10-1-12 0v4H6z" fill="#fff"/>
        <rect x="10" y="19" width="20" height="14" rx="3" fill="#fff"/>
        <circle cx="20" cy="26" r="3.5" fill="#c85a0c"/>
      </svg>
      <svg viewBox="0 0 40 40" aria-hidden="true">
        <rect x="5" y="10" width="30" height="21" fill="#fff"/>
        <path d="M5 10l15 12 15-12" fill="none" stroke="#c85a0c" stroke-width="2"/>
      </svg>
    </div>

    <div class="band-grey"></div>
    <div class="band-orange"></div>
  </section>
</main>
</body>
</html>
```